Kestle Plumbing & Heating Limited needs a service and maintenance contract document design

Kestle Plumbing & Heating Limited are a well established family owned and operated company.

We currently offer installation, service and repair services for gas, plumbing, heating and electrical work. We wish to offer service and maintenance plans for plumbing, heating and electrical for our domestic clients in the UK. We would like the brochure to incorporate our company logo and colours, and reflect the reliable, quality, 5 star service we offer our clients.
I have attached a brochure that a friends company uses to give a good idea of the structure of the plans we wish to offer. We want to give our customers a choice in what packages best suit their needs. However, the pricing structure and certain elements/content of what we offer will be slightly different due to our geographical location.

We would like to have the basic structure of the brochure put in place and the
text content editable to our specific needs. Looking for advice on this but we do have Acrobat DC if we need to edit the text ourselves?

We use our logo with "KESTLE" in white over a grey backgound.

Our website is - www.kestle.example
Facebook and twitter handle is - @KestleHeating

Target Market(s)

UK domestic plumbing, heating, natural gas, LPG and electrical market. Both private homeowners and landlords. Please see both the domestic and landlord document files attached for an idea on what we'd like.

Colors

Designer to choose colors to be used in the design.

Requirements
Must have
• Would like the finished design to incorporate the branding and colours we already use. Professional, Contemporary designs that will stand out above our competition.
• The content of the brochures MUST be very similar in structure to the files I’ve attached to the brief.
• We are having many designs submitted that are just copying our website content. This is not what we are asking for.
• I would like the icons etc to be redesigned so they are ours and not copied.
• Please also see the Landlords brochure attached to the brief. We would like this to be a separate document but to reflect the same design as the homeowner design you submit.
• The content of the documents will need to be re worded for our own use but I'm happy to change this once the design element is in place.
• A4 sized pages as per the example I've attached
• Must be able to attach the document to our website for clients to download.
Nice to have
• A4 sized pages as per the examples I've attached
Should not have
• Please DO NOT copy the content from our website to create our service plan brochures. This is not what we are after. As above, we need the brochures to be like the ones we've provided but made to fit our brand.
• Thank you

```html
<!DOCTYPE html>
<html lang="en">
<head>
<meta charset="utf-8">
<title>Kestle Plumbing &amp; Heating – We Care</title>
<link rel="stylesheet" href="https://fonts.googleapis.com/css2?family=Dancing+Script:wght@600&family=Lato:wght@400;700;900&display=swap">
<style>
  :root {
    --page-bg: #2d2d2d;
    --card-light: #3fa6e6;
    --card-mid: #1e8ed8;
    --card-dark: #0f6fb8;
    --ink-white: #ffffff;
    --badge-fill: #f5d10e;
  }
  * { margin: 0; padding: 0; box-sizing: border-box; }
  html, body {
    width: 861px; height: 1200px; overflow: hidden;
    background: var(--page-bg);
    font-family: "Lato", Arial, sans-serif;
    color: var(--ink-white);
  }
  .sheet { position: relative; width: 861px; height: 1200px; }
  .sheet-title {
    position: absolute; top: 52px; left: 0; width: 100%;
    text-align: center; font-size: 38px; font-weight: 400;
  }
  .care-card {
    position: absolute; left: 95px; top: 195px; width: 686px; height: 801px;
    border-top-left-radius: 58px;
    background: radial-gradient(ellipse at 45% 45%, var(--card-light) 0%, var(--card-mid) 55%, var(--card-dark) 100%);
  }
  .care-heading {
    position: absolute; left: 88px; top: 0px;
    font-family: "Dancing Script", cursive;
    font-size: 122px; font-weight: 600; line-height: 1.2;
    letter-spacing: 2px; white-space: nowrap;
  }
  .care-intro {
    position: absolute; left: 92px; top: 143px;
    font-size: 45px; font-weight: 700; white-space: nowrap;
  }
  .service-list {
    position: absolute; left: 92px; top: 214px; list-style: none;
  }
  .service-item {
    display: flex; align-items: center; height: 60.5px;
    font-size: 54px; font-weight: 700; white-space: nowrap;
  }
  .service-icon {
    width: 43px; height: 43px; margin-right: 28px; flex: none;
    fill: none; stroke: var(--ink-white); stroke-width: 2.4;
    stroke-linecap: round; stroke-linejoin: round;
  }
  .register-badge {
    position: absolute; right: 36px; bottom: 40px;
    width: 150px; height: 150px; border-radius: 14px;
    background: var(--badge-fill);
  }
</style>
</head>
<body>
<main class="sheet">
  <h1 class="sheet-title">Icons</h1>

  <section class="care-card">
    <h2 class="care-heading">We Care</h2>
    <p class="care-intro">We can care for your</p>
    <ul class="service-list">
      <li class="service-item">
        <svg class="service-icon" viewBox="0 0 42 42"><rect x="9" y="3" width="24" height="32" rx="2"/><line x1="9" y1="12" x2="33" y2="12"/><circle cx="21" cy="24" r="4"/><line x1="16" y1="35" x2="16" y2="40"/><line x1="26" y1="35" x2="26" y2="40"/></svg>
        Boiler
      </li>
      <li class="service-item">
        <svg class="service-icon" viewBox="0 0 42 42"><path d="M8 26a13 13 0 0 1 26 0"/><path d="M13 27a8 8 0 0 1 16 0"/><circle cx="21" cy="28" r="3"/></svg>
        Controls
      </li>
      <li class="service-item">
        <svg class="service-icon" viewBox="0 0 42 42"><rect x="4" y="8" width="34" height="26" rx="2"/><line x1="11" y1="8" x2="11" y2="34"/><line x1="17" y1="8" x2="17" y2="34"/><line x1="23" y1="8" x2="23" y2="34"/><line x1="29" y1="8" x2="29" y2="34"/><line x1="8" y1="34" x2="8" y2="39"/><line x1="34" y1="34" x2="34" y2="39"/></svg>
        Central heating
      </li>
      <li class="service-item">
        <svg class="service-icon" viewBox="0 0 42 42"><path d="M6 12h14v10h10v14"/><path d="M6 18h8v10h10v8"/><line x1="14" y1="6" x2="14" y2="12"/><line x1="10" y1="6" x2="18" y2="6"/><path d="M33 10c2 3 2 5 0 6"/></svg>
        Plumbing
      </li>
      <li class="service-item">
        <svg class="service-icon" viewBox="0 0 42 42"><rect x="5" y="5" width="32" height="32" rx="2"/><line x1="5" y1="16" x2="37" y2="16"/><line x1="5" y1="26" x2="37" y2="26"/><line x1="16" y1="5" x2="16" y2="37"/><line x1="26" y1="5" x2="26" y2="37"/></svg>
        Drains
      </li>
      <li class="service-item">
        <svg class="service-icon" viewBox="0 0 42 42"><path d="M4 30h16V12h18"/><path d="M4 36h22V18h12"/><circle cx="12" cy="30" r="3"/></svg>
        Gas pipes
      </li>
      <li class="service-item">
        <svg class="service-icon" viewBox="0 0 42 42"><path d="M10 20l10-10 12 12-10 10z"/><line x1="24" y1="8" x2="29" y2="3"/><line x1="32" y1="16" x2="37" y2="11"/><path d="M14 28L5 37"/></svg>
        Electrics
      </li>
      <li class="service-item">
        <svg class="service-icon" viewBox="0 0 42 42"><rect x="4" y="5" width="34" height="6"/><path d="M8 11v27h26V11"/><rect x="13" y="17" width="16" height="21"/><path d="M21 34c-4 0-5-4-2-7 0 2 2 2 2 0 0-2 3-3 3-1 2 3 1 8-3 8z"/></svg>
        Gas fires
      </li>
    </ul>
    <div class="register-badge" role="img" aria-label="Gas registration badge"></div>
  </section>
</main>
</body>
</html>
```